Movie Poster for Crime/Thriller
We need a poster/DVD case which will grab your attention.

Target Market(s)

DVD Buyers and renters

Industry/Entity Type

Movie

Requirements
Must have
• Name of Film: The Quiet Ledger Affair
Pictures of the mask the gang uses.
The words "Greed, Betrayal, Murder, all components of"

```html
<!DOCTYPE html>
<html lang="en">
<head>
<meta charset="utf-8">
<title>The Quiet Ledger Affair — Poster</title>
<link rel="stylesheet" href="https://fonts.googleapis.com/css2?family=Anton&family=Pinyon+Script&display=swap">
<style>
  :root {
    --ink-deep: #050505;
    --ink-charcoal: #1b1b1b;
    --blood-red: #a8211f;
    --mask-cream: #d9d3c3;
    --mask-grey: #8e9293;
    --clown-blue: #2f5f9c;
    --cheek-rose: #c98a84;
    --tagline-white: #ece6e2;
  }
  html, body {
    margin: 0;
    padding: 0;
    overflow: hidden;
    background: var(--ink-deep);
  }
  .poster {
    position: relative;
    width: 849px;
    height: 1200px;
    overflow: hidden;
    background: var(--ink-charcoal);
  }
  .poster__shadow-strip {
    position: absolute;
    left: 0;
    top: 0;
    width: 115px;
    height: 100%;
    background: var(--ink-deep);
  }
  .poster__edge-bar {
    position: absolute;
    right: 0;
    top: 0;
    width: 26px;
    height: 100%;
    background: var(--blood-red);
  }
  .poster__art {
    position: absolute;
    inset: 0;
  }
  .title text {
    font-family: "Anton", "Impact", sans-serif;
    fill: var(--blood-red);
  }
  .tagline {
    position: absolute;
    right: 48px;
    top: 612px;
    margin: 0;
    font-family: "Pinyon Script", "Times New Roman", serif;
    font-size: 38px;
    line-height: 50px;
    color: var(--tagline-white);
    text-align: right;
    transform: rotate(-4deg);
    transform-origin: right top;
  }
  .tagline span { display: block; }
  .tagline span + span { margin-right: 70px; }
</style>
</head>
<body>
  <main class="poster">
    <div class="poster__shadow-strip"></div>
    <div class="poster__edge-bar"></div>

    <svg class="poster__art" width="849" height="1200" viewBox="0 0 849 1200">
      <defs>
        <radialGradient id="plain-mask-tone" cx="45%" cy="50%" r="65%">
          <stop offset="0" stop-color="#9fa3a3"/>
          <stop offset="0.7" stop-color="#84898a"/>
          <stop offset="1" stop-color="#5f6364"/>
        </radialGradient>
        <linearGradient id="clown-mask-tone" x1="0.15" y1="0" x2="0.05" y2="1">
          <stop offset="0" stop-color="var(--clown-blue)"/>
          <stop offset="0.2" stop-color="#6f8fb4"/>
          <stop offset="0.32" stop-color="var(--mask-cream)"/>
          <stop offset="0.62" stop-color="#d8cdc4"/>
          <stop offset="0.85" stop-color="var(--cheek-rose)"/>
          <stop offset="1" stop-color="#cdbfb5"/>
        </linearGradient>
      </defs>

      <g class="title">
        <text x="0" y="240" font-size="230" textLength="195" lengthAdjust="spacingAndGlyphs" transform="rotate(-3 100 150)">The</text>
        <text x="0" y="448" font-size="215" textLength="320" lengthAdjust="spacingAndGlyphs" transform="rotate(-3 160 360)">Quiet</text>
        <text x="30" y="600" font-size="200" textLength="790" lengthAdjust="spacingAndGlyphs" transform="rotate(-4 425 520)">Ledger Affair</text>
        <line x1="30" y1="676" x2="822" y2="590" stroke="var(--blood-red)" stroke-width="5"/>
      </g>

      <path class="mask mask--plain" role="img"
            aria-label="Photograph of the gang's plain grey full-face mask, partly hidden at the left edge"
            d="M0 712 C80 700 168 760 178 900 C188 1050 160 1150 128 1200 L0 1200 Z"
            fill="url(#plain-mask-tone)" opacity="0.88"/>
      <path class="mask mask--clown" role="img"
            aria-label="Photograph of the gang's cracked clown mask: blue brow, white face, green eyes, red cheeks and lips"
            d="M352 640 C470 638 548 720 545 880 C542 1040 470 1196 348 1196 C218 1196 150 1070 152 930 C154 770 236 642 352 640 Z"
            fill="url(#clown-mask-tone)"/>
    </svg>

    <p class="tagline">
      <span>Greed, Betrayal, Murder,</span>
      <span>all components of</span>
    </p>
  </main>
</body>
</html>
```